Creative IT Startup company web site

We are small IT startup based in Japan
We provide IT consulting services and in-house software development.
Currently we are lunching new campaign called "Ideas to reality" also with this campaign we want to build new web site. Please check out our new web site for more info about project: http://v2.brevotrail.com
As yo see there are only text - we need to make this clear, modern and beautiful. We are looking for creative designer to bring this web site to life.

Also some more information can be taken from our old web site: www.brevotrail.com

Target Market(s)

IT entrepreneurs, Small companies, Anyone who has an idea and want to bring it to life.

Industry/Entity Type

It Company

Colors
86cfc6
85cae6

Requirements
Must have
• Single Page layout as a main page (instead of Hone and About)
this page should be called Ideas to Reality.

```html
<!DOCTYPE html>
<html lang="en">
<head>
<meta charset="utf-8">
<title>Brevotrail network – Ideas to Reality</title>
<link href="https://fonts.googleapis.com/css2?family=Noto+Serif:ital,wght@0,400;0,700;1,400;1,700&display=swap" rel="stylesheet">
<style>
:root{
  --green:#7cc631;
  --green-dark:#5fa81f;
  --ink:#3a3a3a;
  --muted:#666;
  --nav-bg:#ececec;
  --dark:#1f1f1f;
  --white:#fff;
}
*{margin:0;padding:0;box-sizing:border-box}
html,body{width:1200px;height:2683px;overflow:hidden}
body{position:relative;background:var(--white);font-family:"Noto Serif",Georgia,serif;color:var(--ink)}
.abs{position:absolute}
.heading{font-style:italic;font-weight:700}

/* header */
.site-header{left:0;top:0;width:1200px;height:100px}
.brand{left:75px;top:24px;display:flex;align-items:center;gap:12px;color:var(--green);font-size:34px;font-weight:400}
.brand-dot{width:42px;height:42px;border-radius:50%;background:var(--green)}
.contact-block{left:618px;top:27px;display:flex;gap:14px;font-size:16px;font-style:italic;color:var(--muted);line-height:24px}
.social{left:895px;top:36px;display:flex;gap:9px}
.social span{width:29px;height:29px;border-radius:50%;background:#c9c9c9}
.social span:first-child{background:#3b5998}

/* nav */
.main-nav{left:0;top:100px;width:1200px;height:50px;background:linear-gradient(#f6f6f6,#e4e4e4);border-top:1px solid #ddd}
.main-nav ul{list-style:none;display:flex;position:absolute;left:75px;top:0;height:50px}
.main-nav li{height:50px;line-height:50px;padding:0 23px;font-size:17px;color:#444;border-right:1px solid #d4d4d4}
.main-nav li.active{background:var(--green);color:var(--white);font-weight:700}
.nav-search{left:1005px;top:100px;width:56px;height:50px;background:#444}
.nav-flag{left:1064px;top:100px;width:58px;height:50px;background:var(--green);padding:10px 8px}
.nav-flag span{display:block;width:100%;height:100%;background:#2c3f8c}

/* hero */
.hero{left:0;top:150px;width:1200px;height:508px;background:radial-gradient(ellipse at 72% 40%,#e6eef5 0%,#9bb4c9 40%,#5e7f9c 75%,#435f7a 100%)}
.hero-title{left:75px;top:240px;font-size:52px;line-height:72px;color:var(--white)}
.hero-text{left:75px;top:414px;width:500px;font-size:14.5px;line-height:26px;color:var(--white)}
.hero-rule{left:0;top:655px;width:1200px;height:5px;background:var(--green)}
.pager{left:490px;top:642px;display:flex;gap:10px}
.pager span{width:32px;height:30px;border-radius:15px;background:var(--white);border:3px solid var(--green);font-size:12px;font-style:italic;color:#bbb;text-align:center;line-height:24px}
.pager span.current{background:#444;border-color:#444;color:var(--white)}

/* welcome */
.welcome-title{left:0;top:704px;width:1200px;text-align:center;font-size:34px;color:#555}
.welcome-title em{color:var(--green);font-style:italic}
.welcome-text{left:90px;top:772px;width:1020px;text-align:center;font-size:14px;line-height:26px;color:var(--muted)}

/* services */
.services-band{left:0;top:960px;width:1200px;height:220px;background:var(--green)}
.service{top:880px;width:370px;text-align:center;color:var(--white)}
.service-badge{display:block;margin:0 auto;width:124px;height:124px}
.service h3{margin-top:4px;font-size:20px;line-height:28px}
.service p{margin:8px auto 0;width:330px;font-size:14.5px;line-height:25px}
.read-more{top:1148px;width:110px;height:32px;background:var(--white);color:#888;font-size:13px;font-style:italic;font-weight:700;text-align:center;line-height:32px}

/* build idea */
.build{left:0;top:1180px;width:1200px;height:385px;background:linear-gradient(90deg,#f4f4f4,#e2e2e2 60%,#f2f2f2)}
.build-title{left:75px;top:1220px;font-size:32px;color:var(--green)}
.build-rule{left:75px;top:1280px;width:256px;height:4px;background:#ccc}
.build-lead{left:75px;top:1304px;font-size:16px;font-style:italic;font-weight:700;color:#222}
.build-text{left:75px;top:1348px;width:655px;font-size:14.5px;line-height:25px;color:#555}
.blob{width:100%;height:100%}

/* team */
.team-title{left:0;top:1596px;width:1200px;text-align:center;font-size:32px;color:var(--green)}
.team-sub{left:0;top:1650px;width:1200px;text-align:center;font-size:17px;font-style:italic;color:#444}
.member{top:1700px;width:228px;height:262px}

/* tweet */
.tweet-band{left:0;top:1994px;width:1200px;height:191px;background:linear-gradient(#e8e8e8,#cfcfcf 50%,#e4e4e4)}
.tweet{left:75px;top:2035px;width:1050px;height:106px;background:var(--white);border-left:5px solid var(--green);border-right:5px solid var(--green)}
.tweet-icon{left:22px;top:36px;width:36px;height:30px;border-radius:50%;background:var(--green)}
.tweet-text{left:80px;top:28px;width:780px;font-size:16px;line-height:24px;color:#444}
.tweet-text em{color:var(--green);font-style:normal}
.tweet-time{right:18px;top:38px;font-size:17px;color:var(--green)}

/* footer */
.site-footer{left:0;top:2185px;width:1200px;height:443px;background:linear-gradient(#2b2b2b,#1c1c1c 40%,#252525)}
.footer-tabs{left:75px;top:2185px;display:flex}
.footer-tabs div{width:350px;height:55px;line-height:55px;text-align:center;font-size:20px;color:var(--white);background:#4a4a4a;border-left:2px solid #2a2a2a}
.footer-tabs div.active{background:#262626;color:var(--green);border-left:none}
.footer-heading{left:75px;top:2310px;font-size:17px;color:var(--green)}
.contact-list{top:2396px;font-size:15px;line-height:37px}
.contact-list dt{color:var(--green);font-style:italic;font-weight:700;text-align:right}
.contact-row{display:flex;gap:8px}
.contact-row dd{color:var(--white)}
.map{left:818px;top:2310px;width:300px;height:300px;border-radius:50%;border:5px solid #555;background:radial-gradient(circle at 45% 45%,#f1efe9,#dedbd2 70%,#cfcabd)}
.bottom-bar{left:0;top:2628px;width:1200px;height:55px;background:var(--white);font-size:13.5px;line-height:55px;color:#555}
.bottom-bar .links{position:absolute;left:75px}
.bottom-bar .legal{position:absolute;right:75px}
.bottom-bar .hl{color:var(--green)}
</style>
</head>
<body>

<header class="abs site-header">
  <div class="abs brand"><span class="brand-dot"></span>Brevotrail network</div>
  <div class="abs contact-block">
    <svg width="28" height="24" viewBox="0 0 28 24" style="margin-top:12px"><rect x="1" y="6" width="24" height="17" rx="2" fill="#7cc631"/><path d="M1 7l12 9 12-9" stroke="#fff" stroke-width="2" fill="none"/></svg>
    <div>Call: +81 6 5550 1234<br>info@brevotrail.com</div>
  </div>
  <div class="abs social"><span></span><span></span><span></span><span></span><span></span><span></span></div>
</header>

<nav class="abs main-nav">
  <ul>
    <li class="active">Home</li><li>Ideas to Reality</li><li>IT Consulting</li><li>Software Development</li><li>Carriers</li><li>Contact Us</li>
  </ul>
</nav>
<div class="abs nav-search">
  <svg width="56" height="50" viewBox="0 0 56 50"><circle cx="26" cy="23" r="8" stroke="#fff" stroke-width="3" fill="none"/><path d="M32 29l7 7" stroke="#fff" stroke-width="4"/></svg>
</div>
<div class="abs nav-flag" role="img" aria-label="English language flag"><span></span></div>

<section class="abs hero" role="img" aria-label="Photo of glowing light bulbs on a blue background"></section>
<h1 class="abs heading hero-title">We bring your<br>IDEAS to REALITY</h1>
<p class="abs hero-text">In May of 1899 Walter Brandt wrote a letter to the Halvorsen Institute with an idea in mind. On December 17, 1903 Walter, and his brother Oskar, invented and built the world's first airplane — and conducted the world's first successfully controlled, powered and heavier-than-air flight.</p>
<div class="abs hero-rule"></div>
<div class="abs pager"><span>01</span><span>02</span><span class="current">03</span><span>04</span><span>05</span></div>

<h2 class="abs heading welcome-title">Welcome to <em>Brevotrail network</em></h2>
<p class="abs welcome-text">Lorem ipsum dolor sit amet, consectetur adipiscing elit. In ut ligula vitae dolor faucibus commodo accumsan nec lectus. Fusce ac magna vel urna semper dapibus. Sed non malesuada massa, eget tincidunt lectus. Ut eget ullamcorper turpis. Aliquam sit amet diam egestas, interdum orci at, sodales risus. Integer suscipit in magna eu sagittis. Morbi nec neque orci.</p>

<div class="abs services-band"></div>
<div class="abs service" style="left:43px">
  <svg class="service-badge" viewBox="0 0 124 124"><path d="M62 2C95 2 118 22 118 62v62H6V62C6 22 29 2 62 2z" fill="#7cc631"/><circle cx="62" cy="62" r="42" fill="#fff"/><path d="M50 50l-12 12 12 12M74 50l12 12-12 12M66 46l-8 32" stroke="#7cc631" stroke-width="4" fill="none" stroke-linecap="round"/></svg>
  <h3 class="heading">Software Development</h3>
  <p>After many years in Software Project Delivery, Brevotrail network can help you at every stage of your project.</p>
</div>
<div class="abs service" style="left:415px">
  <svg class="service-badge" viewBox="0 0 124 124"><path d="M62 2C95 2 118 22 118 62v62H6V62C6 22 29 2 62 2z" fill="#7cc631"/><circle cx="62" cy="62" r="42" fill="#fff"/><rect x="44" y="44" width="36" height="28" rx="2" stroke="#7cc631" stroke-width="4" fill="none"/><path d="M54 80h16M62 72v8" stroke="#7cc631" stroke-width="4"/><rect x="54" y="52" width="10" height="12" fill="#7cc631"/></svg>
  <h3 class="heading">Application Management</h3>
  <p>90% of the cost involved in managing software systems lies in maintenance phase – which is often neglected</p>
</div>
<div class="abs service" style="left:783px">
  <svg class="service-badge" viewBox="0 0 124 124"><path d="M62 2C95 2 118 22 118 62v62H6V62C6 22 29 2 62 2z" fill="#7cc631"/><circle cx="62" cy="62" r="42" fill="#fff"/><circle cx="62" cy="58" r="12" fill="#7cc631"/><rect x="56" y="70" width="12" height="10" fill="#7cc631"/><path d="M62 36v-6M44 44l-5-5M80 44l5-5M40 58h-6M84 58h6" stroke="#7cc631" stroke-width="3"/></svg>
  <h3 class="heading">Improvement Management</h3>
  <p>We live today in a very high-paced society – organization who wish to excels will need to constantly evolve and innovate.</p>
</div>
<div class="abs read-more" style="left:173px">Read more</div>
<div class="abs read-more" style="left:545px">Read more</div>
<div class="abs read-more" style="left:913px">Read more</div>

<section class="abs build" role="img" aria-label="Blurred photo of a crowd in the background"></section>
<h2 class="abs heading build-title">Build your IDEA</h2>
<div class="abs build-rule"></div>
<p class="abs build-lead">We help to give you the means, the resources, and the people.</p>
<p class="abs build-text">Lorem ipsum dolor sit amet, consectetur adipiscing elit. Donec ut nisl sed eros venenatis fermentum at sit amet felis. Curabitur et magna dui. Integer ipsum neque, lobortis nec luctus eget, facilisis non nisi. Vivamus ultricies erat vel lorem sodales suscipit. Nam eleifend diam sit amet mi mattis graida. Phasellus arcu dolor, varius ac iaculis ut, ullamcorper vel ipsum. Morbi velit nisi, vulputate id tnt eu, ullamcorper quis arcu. In hac habitasse platea dictumst. Nam era vt ligula, congue id enim ac, malesuada dapibus mi.</p>
<div class="abs" style="left:772px;top:1208px;width:262px;height:330px">
  <svg class="blob" viewBox="0 0 262 330"><path d="M40 20C90-10 200 0 240 40c30 40 25 200 5 250-20 45-180 50-215 10C0 260-10 60 40 20z" fill="#7cc631"/><ellipse cx="133" cy="165" rx="106" ry="130" fill="#fff"/><ellipse cx="133" cy="165" rx="92" ry="115" fill="#c7a86a" role="img" aria-label="Photo of a colourful toy construction model"/></svg>
</div>

<h2 class="abs heading team-title">Meet Your TEAM</h2>
<p class="abs team-sub">We have the developers, project managers, designers and professionals for your team .</p>
<div class="abs member" style="left:75px"><svg class="blob" viewBox="0 0 228 262"><path d="M30 20C80-5 180-5 210 30c25 40 20 170 0 205-25 35-165 35-190 5C-5 200-5 50 30 20z" fill="#7cc631"/><ellipse cx="117" cy="135" rx="88" ry="105" fill="#6f6f6f" role="img" aria-label="Portrait of a team member"/></svg></div>
<div class="abs member" style="left:350px"><svg class="blob" viewBox="0 0 228 262"><path d="M30 20C80-5 180-5 210 30c25 40 20 170 0 205-25 35-165 35-190 5C-5 200-5 50 30 20z" fill="#7cc631"/><ellipse cx="117" cy="135" rx="88" ry="105" fill="#5a5a5a" role="img" aria-label="Portrait of a team member"/></svg></div>
<div class="abs member" style="left:625px"><svg class="blob" viewBox="0 0 228 262"><path d="M30 20C80-5 180-5 210 30c25 40 20 170 0 205-25 35-165 35-190 5C-5 200-5 50 30 20z" fill="#7cc631"/><ellipse cx="117" cy="135" rx="88" ry="105" fill="#4c4c4c" role="img" aria-label="Portrait of a team member"/></svg></div>
<div class="abs member" style="left:900px"><svg class="blob" viewBox="0 0 228 262"><path d="M30 20C80-5 180-5 210 30c25 40 20 170 0 205-25 35-165 35-190 5C-5 200-5 50 30 20z" fill="#7cc631"/><ellipse cx="117" cy="135" rx="88" ry="105" fill="#626262" role="img" aria-label="Portrait of a team member"/></svg></div>

<section class="abs tweet-band" role="img" aria-label="Blurred office photo in the background"></section>
<div class="abs tweet">
  <span class="abs tweet-icon"></span>
  <p class="abs tweet-text">Lorem ipsum dolor sit amet, consectetur adipiscing elit. <em>Aenean hendrerit,</em> tellus in fermentum pellentesque . consectetur adipiscing elit</p>
  <span class="abs heading tweet-time">2 hour ago</span>
</div>

<footer class="abs site-footer" role="img" aria-label="Dark blurred city photo in the background"></footer>
<div class="abs footer-tabs">
  <div class="heading active">Japan Get in Touch!</div>
  <div class="heading">Spain Get in Touch!</div>
  <div class="heading">Ireland Get in Touch!</div>
</div>
<h3 class="abs heading footer-heading">E-Mail &amp; Location</h3>
<dl class="abs contact-list" style="left:75px">
  <div class="contact-row"><dt style="width:138px">General enquires:</dt><dd>info@brevotrail.com</dd></div>
  <div class="contact-row"><dt style="width:138px">Support:</dt><dd>support@brevotrail.com</dd></div>
  <div class="contact-row"><dt style="width:138px">Sales:</dt><dd>sales@brevotrail.com</dd></div>
  <div class="contact-row"><dt style="width:138px">Sourcing:</dt><dd>sourcing@brevotrail.com</dd></div>
</dl>
<dl class="abs contact-list" style="left:440px;line-height:25px">
  <div class="contact-row" style="height:57px"><dt style="width:115px">Osaka Office:</dt><dd>2-7-15 Minamimori, Kitaku,<br>Osakashi Osaka, Japan 530-0054</dd></div>
  <div class="contact-row" style="height:57px"><dt style="width:115px">Tokyo Office:</dt><dd>141-0031 Tokyo-to, Shinagawa-ku,<br>Nishi 5-18-3</dd></div>
  <div class="contact-row"><dt style="width:115px">Phone:</dt><dd>+81 6 5550 1234</dd></div>
</dl>
<div class="abs map" role="img" aria-label="Street map of the Osaka office location"></div>

<div class="abs bottom-bar">
  <span class="links"><span class="hl">Home</span> / Ideas to Reality / IT Consulting / Software Development / Carriers / Contact Us</span>
  <span class="legal">© 2014 <span class="hl">Brevotrail network.</span> Privacy Policy / Term of Use / Site Map</span>
</div>

</body>
</html>
```